Business card for my new company (Accounting firm)

I need a business card for my new business Corvane Advisory and Ledger SA. Our services are accounting, tax, audit and financial management. Our customers are small companies, start-ups and new companies. The final design has to show financial security, trust and growth. Please find our logo attached to the business card. Text for the business card: Corvane Advisory and Ledger SA Tomas da Varela Director and Founder Certified Accountant Tel. 022 418 27 35 tv@corvaneconseil.ch www.corvaneconseil.ch Rue des Vergers-Bleus 14 1201 Geneva
Target Market(s)
Our customers are small companies, start-ups and new companies.
Industry/Entity Type
Finance And Accounting
Contact Information for Business Card
Corvane Conseil et Registre SA
Tomas da Varela
Directeur et Fondateur
Expert-comptable diplômé
Tél. 022 418 27 35
tv@corvaneconseil.ch
www.corvaneconseil.ch
Rue des Vergers-Bleus 14
1201 Genève

```html
<!DOCTYPE html>
<html lang="fr">
<head>
<meta charset="utf-8">
<title>Corvane Conseil et Registre SA — Carte de visite</title>
<link rel="stylesheet" href="https://fonts.googleapis.com/css2?family=Teko:wght@400;500&family=Montserrat:wght@400;500;600&family=Encode+Sans+Condensed:wght@400&display=swap">
<style>
  :root {
    --page: #ffffff;
    --card-bg: #eef8fa;
    --brand-blue: #0a45f7;
    --ink-dark: #2f3a3a;
    --white: #ffffff;
    --divider: #3aa0f5;
  }
  * { margin: 0; padding: 0; box-sizing: border-box; }
  html, body {
    width: 1200px; height: 621px; overflow: hidden;
    background: var(--page);
    font-family: "Montserrat", Arial, sans-serif;
  }
  .canvas { position: relative; width: 1200px; height: 621px; }

  .card {
    position: absolute; top: 115px; width: 508px; height: 290px;
    background: var(--card-bg); overflow: hidden;
  }
  .card--front { left: 97px; }
  .card--back { left: 606px; }

  .front-band { position: absolute; left: 0; top: 0; }

  .brand {
    position: absolute; left: 36px; top: 172px;
    color: var(--ink-dark); font-weight: 500;
    display: flex; align-items: center; gap: 10px;
  }
  .brand-dot { width: 14px; height: 14px; border-radius: 50%; background: var(--ink-dark); }
  .brand-name { font-size: 34px; letter-spacing: 3px; line-height: 1; }
  .brand-sub {
    position: absolute; left: 36px; top: 220px;
    font-size: 14px; letter-spacing: 3px; color: var(--ink-dark); font-weight: 500;
  }

  .front-name {
    position: absolute; right: 12px; top: 22px;
    font-family: "Teko", "Arial Narrow", sans-serif; font-weight: 500;
    font-size: 32px; line-height: 1; letter-spacing: 4px; color: var(--white);
    white-space: nowrap;
  }
  .front-rule { position: absolute; left: 259px; right: 0; top: 70px; height: 2px; background: var(--white); }
  .front-role {
    position: absolute; right: 12px; top: 80px;
    font-size: 13px; letter-spacing: 2.8px; color: var(--white); white-space: nowrap;
  }
  .front-phone {
    position: absolute; right: 12px; top: 209px;
    font-size: 17px; font-weight: 600; letter-spacing: 1px; color: var(--white);
    white-space: nowrap;
  }

  .back-band { position: absolute; left: 0; top: 19px; width: 508px; height: 216px; background: var(--brand-blue); }
  .address {
    position: absolute; left: 21px; top: 38px;
    font-size: 14px; line-height: 23px; letter-spacing: 2px; color: var(--white);
  }
  .identity {
    position: absolute; right: 17px; top: 38px; text-align: right; color: var(--white);
  }
  .identity-name {
    font-family: "Teko", "Arial Narrow", sans-serif; font-weight: 500;
    font-size: 30px; line-height: 22px; letter-spacing: 3px; padding-top: 4px;
  }
  .identity-role { font-size: 14px; letter-spacing: 2.5px; margin-top: 2px; }
  .identity-title {
    font-family: "Encode Sans Condensed", "Arial Narrow", sans-serif;
    font-size: 14px; letter-spacing: 2px; margin-top: 3px;
  }
  .identity-phone { font-size: 15px; font-weight: 600; letter-spacing: 3.5px; margin-top: 3px; }
  .company {
    position: absolute; left: 0; right: 0; top: 209px; text-align: center;
    font-size: 18px; font-weight: 500; letter-spacing: 1.5px; color: var(--white);
  }
  .contact {
    position: absolute; top: 245px; font-size: 15px; letter-spacing: 1.2px;
    color: var(--brand-blue); white-space: nowrap;
  }
  .contact--email { left: 21px; }
  .contact--web { right: 21px; }
  .contact-divider { position: absolute; left: 253px; top: 250px; width: 2px; height: 18px; background: var(--divider); }
</style>
</head>
<body>
<div class="canvas">
  <section class="card card--front">
    <svg class="front-band" width="508" height="290" viewBox="0 0 508 290" aria-hidden="true">
      <polygon points="206,19 508,19 508,235 334,235" fill="var(--brand-blue)"/>
    </svg>
    <div class="brand"><span class="brand-dot"></span><span class="brand-name">CORVANE</span></div>
    <div class="brand-sub">CONSEIL ET REGISTRE</div>
    <div class="front-name">TOMAS DA VARELA</div>
    <div class="front-rule"></div>
    <div class="front-role">Directeur et Fondateur</div>
    <div class="front-phone">Tél. 022 418 27 35</div>
  </section>

  <section class="card card--back">
    <div class="back-band"></div>
    <div class="address">Rue des Vergers-Bleus 14<br>1201 Genève</div>
    <div class="identity">
      <div class="identity-name">TOMAS DA VARELA</div>
      <div class="identity-role">Directeur et Fondateur</div>
      <div class="identity-title">Expert-comptable diplômé</div>
      <div class="identity-phone">Tél. 022 418 27 35</div>
    </div>
    <div class="company">CORVANE CONSEIL ET REGISTRE SA</div>
    <div class="contact contact--email">tv@corvaneconseil.ch</div>
    <div class="contact-divider"></div>
    <div class="contact contact--web">www.corvaneconseil.ch</div>
  </section>
</div>
</body>
</html>
```